Natural and organic skincare brand needs label design!

I need labels designed for my natural and organic skincare brand lumavale. The front of the bottles must contain the logo (image attached) and the following words: Formulated by a Naturopath; Anti-aging therapy; Organic Facial Oil; with CoEnzyme Q10 and Rosehip Seed Oil; 100ml e3.38fl.oz. Colours I would like used include black/white/grey/silver and aqua. I also like the grey woodgrain used on my draft website (check out www.lumavale-skin.com.au). The logo should be silver foil (shiny).The final design should be simple and communicate nature and sophistication. Some designs I like are found in the attachments. I intend to use black or white bottles.

Target Market(s)

women aged 30-50 interested in natural products

Industry/Entity Type

Skin Care Product

Font styles to use
Serif
Sans Serif
Decorative
Script
Other font styles liked:
• Any

Requirements
Must have
• Dimensions: 62mm (w) x 75mm (H) (front label only)
• Must contain the logo (image attached). The logo should be silver foil (shiny). and the following words are to be included on the label:
• Formulated by a Naturopath;
• Anti-aging Therapy;
• Organic Facial Oil;
• with CoEnzyme Q10 and Rosehip Seed Oil;
• 100ml e3.38fl.oz.
Nice to have
• Colours I would like used include black/white/grey/silver and aqua (turquoise). But I am also open to suggestion. I also like the grey woodgrain used on my draft website (check out www.lumavale-skin.com.au)

```html
<!DOCTYPE html>
<html lang="en">
<head>
<meta charset="utf-8">
<title>lumavale – Organic Facial Oil Labels</title>
<link href="https://fonts.googleapis.com/css2?family=Cinzel:wght@400;500&family=Oswald:wght@500&family=Roboto+Condensed:wght@300;400&display=swap" rel="stylesheet">
<style>
  :root {
    --page: #ffffff;
    --silver-light: #c9c9c9;
    --silver-dark: #8d8d8d;
    --aqua: #39b9b0;
    --aqua-soft: #a6e2dc;
    --grey: #a3a3a3;
    --grey-soft: #dedede;
    --black: #0c0c0c;
    --charcoal: #3a3a3a;
    --tan: #d4aa79;
    --tan-deep: #9b7b57;
    --bark: #5f4b3a;
  }
  * { margin: 0; padding: 0; box-sizing: border-box; }
  html, body { width: 1200px; height: 1145px; overflow: hidden; background: var(--page); }
  .label-row {
    position: absolute; top: 412px; left: 36px;
    display: flex; gap: 24px;
  }
  .label {
    position: relative; width: 264px; height: 320px;
    background: var(--bg); color: var(--ink);
    overflow: hidden;
  }
  .label--aqua  { --bg: #ffffff; --ink: #222; --accent: var(--aqua); --strip-a: var(--aqua-soft); --strip-b: var(--aqua); --disc-a: var(--silver-light); --disc-b: var(--silver-dark); --name: #ffffff; }
  .label--grey  { --bg: #ffffff; --ink: #222; --accent: var(--grey); --strip-a: var(--grey-soft); --strip-b: var(--grey); --disc-a: var(--silver-light); --disc-b: var(--silver-dark); --name: #ffffff; }
  .label--black { --bg: var(--black); --ink: #ffffff; --accent: #ffffff; --strip-a: #1e1e1e; --strip-b: #5a5a5a; --disc-a: #9a9a9a; --disc-b: #5c5c5c; --name: #ffffff; }
  .label--tan   { --bg: var(--tan); --ink: #2e241c; --accent: var(--bark); --strip-a: var(--tan); --strip-b: var(--tan-deep); --disc-a: #9c8b78; --disc-b: #6a5a4a; --name: #f1e6d8; }

  .pattern-strip {
    position: absolute; top: 0; right: 0; width: 38px; height: 100%;
    background: linear-gradient(180deg, var(--strip-a), var(--strip-b) 50%, var(--strip-a));
    opacity: .85;
  }
  .label-body { position: absolute; top: 0; left: 0; width: 226px; height: 100%; text-align: center; }
  .arc-title { position: absolute; top: 14px; left: 0; width: 226px; height: 70px; }
  .arc-title text {
    font-family: 'Roboto Condensed', sans-serif; font-weight: 400; font-size: 15px;
    fill: var(--ink); letter-spacing: .3px;
  }
  .brand-disc {
    position: absolute; top: 44px; left: 55px; width: 116px; height: 116px; border-radius: 50%;
    background: radial-gradient(circle at 35% 30%, var(--disc-a), var(--disc-b));
    border: 2px solid var(--disc-a);
    display: flex; align-items: center; justify-content: center;
  }
  .brand-name {
    font-family: 'Roboto Condensed', sans-serif; font-weight: 300; font-size: 22px;
    color: var(--name); letter-spacing: 2px;
  }
  .formulated {
    position: absolute; top: 176px; left: 0; width: 226px;
    font-family: 'Cinzel', serif; font-size: 12px; line-height: 15px; color: var(--ink);
  }
  .product-name {
    position: absolute; top: 214px; left: 0; width: 226px;
    font-family: 'Oswald', sans-serif; font-weight: 500; font-size: 25px; line-height: 27px;
    color: var(--accent); text-transform: uppercase;
  }
  .ingredients {
    position: absolute; top: 270px; left: 0; width: 226px;
    font-family: 'Roboto Condensed', sans-serif; font-size: 9.5px; line-height: 11px; color: var(--ink);
  }
  .volume {
    position: absolute; top: 298px; left: 0; width: 226px; text-align: right; padding-right: 8px;
    font-family: 'Roboto Condensed', sans-serif; font-size: 10.5px; color: var(--ink);
  }
</style>
</head>
<body>
<main class="label-row">
  <section class="label label--aqua">
    <div class="pattern-strip" role="img" aria-label="Aqua floral pattern band"></div>
    <div class="label-body">
      <svg class="arc-title" viewBox="0 0 226 70"><path id="arc1" d="M38 76 A76 76 0 0 1 188 76" fill="none"/><text><textPath href="#arc1" startOffset="50%" text-anchor="middle">ORGANIC FACIAL OIL</textPath></text></svg>
      <div class="brand-disc"><span class="brand-name">lumavale</span></div>
      <p class="formulated">Formulated by<br>a Naturopath</p>
      <h2 class="product-name">Anti-Aging<br>Therapy</h2>
      <p class="ingredients">with CoEnzyme Q10<br>and Rosehip Seed Oil</p>
      <p class="volume">100ml e 3.38fl.oz.</p>
    </div>
  </section>
  <section class="label label--grey">
    <div class="pattern-strip" role="img" aria-label="Silver grey floral pattern band"></div>
    <div class="label-body">
      <svg class="arc-title" viewBox="0 0 226 70"><path id="arc2" d="M38 76 A76 76 0 0 1 188 76" fill="none"/><text><textPath href="#arc2" startOffset="50%" text-anchor="middle">ORGANIC FACIAL OIL</textPath></text></svg>
      <div class="brand-disc"><span class="brand-name">lumavale</span></div>
      <p class="formulated">Formulated by<br>a Naturopath</p>
      <h2 class="product-name">Anti-Aging<br>Therapy</h2>
      <p class="ingredients">with CoEnzyme Q10<br>and Rosehip Seed Oil</p>
      <p class="volume">100ml e 3.38fl.oz.</p>
    </div>
  </section>
  <section class="label label--black">
    <div class="pattern-strip" role="img" aria-label="Dark grey floral pattern band"></div>
    <div class="label-body">
      <svg class="arc-title" viewBox="0 0 226 70"><path id="arc3" d="M38 76 A76 76 0 0 1 188 76" fill="none"/><text><textPath href="#arc3" startOffset="50%" text-anchor="middle">ORGANIC FACIAL OIL</textPath></text></svg>
      <div class="brand-disc"><span class="brand-name">lumavale</span></div>
      <p class="formulated">Formulated by<br>a Naturopath</p>
      <h2 class="product-name">Anti-Aging<br>Therapy</h2>
      <p class="ingredients">with CoEnzyme Q10<br>and Rosehip Seed Oil</p>
      <p class="volume">100ml e 3.38fl.oz.</p>
    </div>
  </section>
  <section class="label label--tan">
    <div class="pattern-strip" role="img" aria-label="Brown floral pattern band"></div>
    <div class="label-body">
      <svg class="arc-title" viewBox="0 0 226 70"><path id="arc4" d="M38 76 A76 76 0 0 1 188 76" fill="none"/><text><textPath href="#arc4" startOffset="50%" text-anchor="middle">ORGANIC FACIAL OIL</textPath></text></svg>
      <div class="brand-disc"><span class="brand-name">lumavale</span></div>
      <p class="formulated">Formulated by<br>a Naturopath</p>
      <h2 class="product-name">Anti-Aging<br>Therapy</h2>
      <p class="ingredients">with CoEnzyme Q10<br>and Rosehip Seed Oil</p>
      <p class="volume">100ml e 3.38fl.oz.</p>
    </div>
  </section>
</main>
</body>
</html>
```